Harbor Business Cards

I need a business card designed with the following information.

Company Name: Harbor Wealth Management
Name: BriAnne Dockery
Title: Executive Assistant
Cell: (281) 555-0173
Direct Line: (832) 555-0148
Email: brianne@harborwmx.com
Address: 20537 W. Marlowe PKWY Ste. B
Tomball, TX 77390

I have attached the logo.
I would like it in navy blue and silver.
Thanks.

```html
<!DOCTYPE html>
<html lang="en">
<head>
<meta charset="utf-8">
<title>Harbor Wealth Management – Business Cards</title>
<link rel="stylesheet" href="https://fonts.googleapis.com/css2?family=PT+Sans:wght@400&display=swap">
<style>
  :root {
    --navy: #10264a;
    --navy-deep: #0c1e3b;
    --silver: #dfe3e8;
    --paper: #ffffff;
    --ghost: #eeeeef;
    --ink: #1b1f26;
    --backdrop: #e6e7e9;
  }
  * { margin: 0; padding: 0; box-sizing: border-box; }
  html, body { width: 1200px; height: 1000px; overflow: hidden; }
  body {
    background: var(--backdrop);
    font-family: "PT Sans", Arial, sans-serif;
    position: relative;
  }
  .card {
    position: absolute;
    left: 220px;
    width: 760px;
    height: 434px;
    overflow: hidden;
    box-shadow: 0 6px 18px rgba(0,0,0,0.18);
  }

  /* Front */
  .card-front {
    top: 44px;
    background: var(--navy);
    display: flex;
    flex-direction: column;
    align-items: center;
    justify-content: center;
    gap: 26px;
  }
  .brand-mark {
    width: 96px;
    height: 96px;
    background: var(--silver);
  }
  .brand-name {
    font-family: "PT Sans", Arial, sans-serif;
    font-weight: 400;
    color: var(--silver);
    font-size: 40px;
    line-height: 1;
  }

  /* Back */
  .card-back {
    top: 522px;
    background: var(--paper);
    display: flex;
  }
  .back-band {
    width: 58px;
    background: var(--navy);
    flex: none;
  }
  .back-ghost {
    position: absolute;
    right: 40px;
    top: 40px;
    width: 250px;
    height: 250px;
    background: var(--ghost);
  }
  .back-content {
    position: relative;
    padding: 34px 0 0 60px;
    color: var(--ink);
  }
  .back-brand {
    display: flex;
    flex-direction: column;
    align-items: flex-start;
    gap: 14px;
  }
  .back-brand .brand-mark {
    width: 58px;
    height: 58px;
    background: var(--navy);
  }
  .back-brand .brand-name {
    color: var(--navy);
    font-size: 28px;
  }
  .person-name {
    margin-top: 26px;
    font-size: 24px;
    color: var(--navy-deep);
  }
  .person-title {
    font-size: 15px;
    margin-top: 2px;
  }
  .contact-list {
    list-style: none;
    margin-top: 20px;
    font-size: 17px;
    line-height: 1.5;
  }
  .contact-list li { display: flex; align-items: center; gap: 8px; }
  .contact-list svg { width: 14px; height: 14px; fill: var(--navy); flex: none; }
</style>
</head>
<body>
  <section class="card card-front" aria-label="Card front">
    <div class="brand-mark" aria-hidden="true"></div>
    <div class="brand-name">Harbor Wealth Management</div>
  </section>

  <section class="card card-back" aria-label="Card back">
    <div class="back-band"></div>
    <div class="back-ghost" aria-hidden="true"></div>
    <div class="back-content">
      <div class="back-brand">
        <div class="brand-mark" aria-hidden="true"></div>
        <div class="brand-name">Harbor Wealth Management</div>
      </div>
      <div class="person-name">BriAnne Dockery</div>
      <div class="person-title">Executive Assistant</div>
      <ul class="contact-list">
        <li>20537 W. Marlowe PKWY Ste. B Tomball, TX 77390</li>
        <li>
          <svg viewBox="0 0 16 16" aria-hidden="true"><path d="M3.5 1.5l2.5 0 1 3.5-1.6 1.2a8 8 0 0 0 4.4 4.4L11 9l3.5 1v2.5c0 1-1 2-2 2C6.5 14.5 1.5 9.5 1.5 3.5c0-1 1-2 2-2z"/></svg>
          Direct Line: (832) 555-0148
        </li>
        <li>
          <svg viewBox="0 0 16 16" aria-hidden="true"><path d="M4.5 0.5h7a1 1 0 0 1 1 1v13a1 1 0 0 1-1 1h-7a1 1 0 0 1-1-1v-13a1 1 0 0 1 1-1zm0.5 2v10h6v-10z"/></svg>
          (281) 555-0173
        </li>
        <li>
          <svg viewBox="0 0 16 16" aria-hidden="true"><path d="M1 3.5h14v9H1zm1.2 1.2v0.4L8 9l5.8-3.9v-0.4z"/></svg>
          brianne@harborwmx.com
        </li>
      </ul>
    </div>
  </section>
</body>
</html>
```